Tamarack Hearth Partners Business Card

Looking for a new business card layout. We are a real estate firm w/ a logo, old design attached. Must keep the same elements on there, just need a fresh look and possible some foil accents. Looking for a simpler design w/ more modern style.

Target Market(s)

Real Estate clients

Industry/Entity Type

Real Estate Agent

Contact Information for Business Card

see attached

Font styles to use
Sans Serif

Requirements
Must have
• all elements on current biz card
Nice to have
• modern look, simpler than we have!
Should not have
• no serif fonts

```html
<!DOCTYPE html>
<html lang="en">
<head>
<meta charset="utf-8">
<title>Tamarack Hearth Partners Business Card</title>
<link href="https://fonts.googleapis.com/css2?family=Poppins:wght@300;400;500;600;700&display=swap" rel="stylesheet">
<style>
  :root{
    --stage:#2a2a2b;
    --card:#1f1f20;
    --card-edge:#262627;
    --ink:#f2f2f2;
    --muted:#9a9a9a;
    --silver:#b9b9bb;
    --accent:#e0262e;
    --photo-a:#e9d6b8;
    --photo-b:#7fb9b3;
  }
  *{margin:0;padding:0;box-sizing:border-box}
  html,body{width:1200px;height:900px;overflow:hidden}
  body{
    background:var(--stage);
    font-family:"Poppins",sans-serif;
    color:var(--ink);
    position:relative;
  }
  .card{
    position:absolute;
    left:285px;
    width:630px;
    height:360px;
    background:linear-gradient(160deg,var(--card-edge),var(--card));
    border-radius:4px;
    box-shadow:0 18px 40px rgba(0,0,0,.45);
    overflow:hidden;
  }
  .card--front{top:50px}
  .card--back{top:490px}

  /* front */
  .agent{
    position:absolute;left:60px;top:48px;width:230px;
    display:flex;flex-direction:column;align-items:center;
  }
  .agent__photo{
    width:170px;height:170px;border-radius:50%;
    background:radial-gradient(circle at 50% 40%,var(--photo-a) 0%,#d8bb8c 45%,var(--photo-b) 100%);
  }
  .agent__name{
    margin-top:26px;font-size:23px;font-weight:600;letter-spacing:.5px;text-transform:uppercase;
  }
  .agent__title{
    margin-top:2px;font-size:12.5px;font-weight:300;color:var(--muted);letter-spacing:.8px;text-transform:uppercase;
  }
  .divider{
    position:absolute;left:318px;top:70px;width:1.5px;height:230px;background:var(--accent);
  }
  .details{position:absolute;left:344px;top:62px;right:24px}
  .brand{
    font-size:22px;font-weight:600;line-height:1.15;letter-spacing:1.5px;
    color:var(--silver);text-transform:uppercase;
  }
  .contact{list-style:none;margin-top:22px}
  .contact li{
    display:flex;align-items:center;gap:9px;font-size:13.5px;font-weight:400;line-height:1;margin-bottom:9px;
  }
  .contact li.strong{font-weight:500}
  .contact svg{width:14px;height:14px;flex:none}
  .address{margin-top:12px;font-size:12.5px;font-weight:300;line-height:1.5}

  /* back */
  .back__inner{
    position:absolute;inset:0;display:flex;flex-direction:column;align-items:center;justify-content:center;
  }
  .back__brand{
    font-size:36px;font-weight:600;line-height:1.15;letter-spacing:2px;text-align:center;
    color:var(--silver);text-transform:uppercase;
  }
  .back__web{
    margin-top:34px;font-size:13px;font-weight:400;letter-spacing:6px;color:var(--muted);text-transform:uppercase;
  }
</style>
</head>
<body>

<section class="card card--front">
  <div class="agent">
    <div class="agent__photo" role="img" aria-label="Portrait photo of the broker"></div>
    <p class="agent__name">Maren Vance</p>
    <p class="agent__title">Principal Broker</p>
  </div>

  <div class="divider"></div>

  <div class="details">
    <p class="brand">Tamarack Hearth<br>Partners</p>

    <ul class="contact">
      <li>
        <svg viewBox="0 0 16 16" aria-hidden="true"><path fill="var(--accent)" d="M3.6 1.5l2.2 2.6-1.3 1.6c.9 2 2.7 3.8 4.8 4.8l1.6-1.3 2.6 2.2-1.3 2.1C7.4 14.9 1.1 8.6 1.5 3z"/></svg>
        <span>Office: <strong>555.210.4817</strong></span>
      </li>
      <li class="strong">
        <svg viewBox="0 0 16 16" aria-hidden="true"><rect x="4" y="1" width="8" height="14" rx="1.5" fill="none" stroke="var(--accent)" stroke-width="1.6"/><circle cx="8" cy="12.3" r="0.9" fill="var(--accent)"/></svg>
        <span>555.374.9062</span>
      </li>
      <li>
        <svg viewBox="0 0 16 16" aria-hidden="true"><rect x="1" y="3" width="14" height="10" rx="1" fill="var(--accent)"/><path d="M1.5 3.8L8 9l6.5-5.2" fill="none" stroke="var(--card)" stroke-width="1.3"/></svg>
        <span>maren@hearthhomesre.com</span>
      </li>
      <li>
        <svg viewBox="0 0 16 16" aria-hidden="true"><g fill="none" stroke="var(--accent)" stroke-width="1.3"><circle cx="8" cy="8" r="6.5"/><ellipse cx="8" cy="8" rx="2.8" ry="6.5"/><path d="M1.5 8h13M2.6 4.6h10.8M2.6 11.4h10.8"/></g></svg>
        <span>TamarackHearth-Homes.com</span>
      </li>
    </ul>

    <p class="address">482 Juniper Ave<br>Bendfield, OR 97000</p>
  </div>
</section>

<section class="card card--back">
  <div class="back__inner">
    <p class="back__brand">Tamarack Hearth<br>Partners</p>
    <p class="back__web">www.tamarackhearth-homes.com</p>
  </div>
</section>

</body>
</html>
```